Redesign Of Current Landing Page

I need to redesign this landing page https://www.brightoakpromos.biz/?page=landing&landing=23 (Please do not opt in because when you do it will show you the home page. Please clear your cookies before going to this url above to view the 1 page landing page.)

Please use my updated website as a reference for colors and logo.
http://layoutcraftzone.com/dh/bopg/index.html

I would like the call to action to be a button that opens into a lead form...

Button would be "Download Samples"

small business owners

Marketing

1 page

Designer to choose colors to be used in the design.

• must be full responsive on all devices
• must have a legitimate professional apeal to it
• open

```html
<!DOCTYPE html>
<html lang="en">
<head>
<meta charset="utf-8">
<title>Bright Oak Promotions Group – Download Samples</title>
<link href="https://fonts.googleapis.com/css2?family=Raleway:wght@300;400;600;700;800&family=Open+Sans:wght@400;600;700&display=swap" rel="stylesheet">
<style>
:root{
  --navy:#0c2340;
  --navy-2:#123a66;
  --blue:#1b75c9;
  --blue-2:#2a8be0;
  --orange:#f39a1e;
  --orange-dark:#d9810a;
  --ink:#2b2f36;
  --muted:#6b7480;
  --light:#f1f3f6;
  --white:#ffffff;
}
*{box-sizing:border-box;margin:0;padding:0}
html,body{width:1200px;height:2340px;overflow:hidden}
body{font-family:"Open Sans",Arial,sans-serif;color:var(--ink);background:var(--white)}
h1,h2,h3,.brand{font-family:"Raleway",Arial,sans-serif}
.btn{display:inline-block;background:var(--orange);color:var(--white);font-family:"Raleway",sans-serif;font-weight:700;font-size:13px;text-transform:uppercase;text-align:center;line-height:1.25;padding:11px 26px;border-radius:3px;border-bottom:3px solid var(--orange-dark)}

/* hero */
.hero{position:relative;height:760px;background:linear-gradient(180deg,#1d3550 0%,#2c4d70 35%,#3f6488 60%,#2a4a6c 100%);color:var(--white)}
.hero-photo{position:absolute;inset:0;background:linear-gradient(160deg,rgba(120,150,180,.35),rgba(10,30,55,.2) 60%,rgba(10,30,55,.55))}
.topbar{position:relative;display:flex;justify-content:space-between;align-items:center;padding:26px 60px}
.brand{display:flex;align-items:center;gap:10px;font-weight:800;font-size:26px;letter-spacing:1px}
.brand .mark{width:16px;height:16px;background:var(--white)}
.contact{text-align:right;font-size:13px;line-height:1.6}
.contact b{color:var(--orange)}
.hero-copy{position:absolute;left:60px;top:150px;width:560px}
.hero-copy h1{font-weight:300;font-size:44px;line-height:1.05;text-transform:uppercase;letter-spacing:1px}
.hero-copy h1 strong{display:block;font-weight:800;font-size:52px}
.hero-copy p{margin-top:18px;font-size:17px;font-weight:600;line-height:1.4;max-width:400px}
.lead-form{position:absolute;right:50px;top:115px;width:330px;background:var(--white);border-top:6px solid var(--blue);box-shadow:0 6px 20px rgba(0,0,0,.3);color:var(--ink)}
.lead-form .head{background:var(--blue);color:var(--white);text-align:center;padding:14px 20px 16px}
.lead-form .head h3{font-size:24px;font-weight:800;text-transform:uppercase}
.lead-form .head p{font-size:11px;margin-top:4px}
.lead-form .body{padding:18px 22px 22px}
.field{height:34px;border:1px solid #cfd5dc;border-radius:2px;margin-bottom:10px;padding:8px 10px;font-size:12px;color:#8a929c}
.lead-form .btn{width:100%;margin-top:6px}

/* imagine */
.imagine{position:relative;height:500px;margin-top:-260px;background:var(--blue)}
.imagine svg.curve{position:absolute;top:-60px;left:0}
.imagine-copy{position:absolute;left:60px;top:50px;width:470px;color:var(--white)}
.imagine-copy h2{font-size:30px;font-weight:800;text-transform:uppercase;letter-spacing:1px}
.imagine-copy p{margin-top:16px;font-size:12px;line-height:1.65}
.imagine-copy .btn{margin-top:22px}
.samples{position:absolute;left:600px;top:20px;width:560px;height:300px;background:linear-gradient(135deg,#1f4e86,#c0392b 45%,#e7b23a 75%,#2e7d4f);border-radius:4px}
.imagine-name{position:absolute;left:600px;top:365px;width:560px;text-align:center;color:var(--white);font-family:"Raleway",sans-serif;font-weight:700;font-size:26px;letter-spacing:1px}

/* how */
.how{height:340px;text-align:center;padding:40px 160px 0}
.sec-title{font-size:30px;font-weight:600;color:var(--ink)}
.dot{width:26px;height:26px;border-radius:50%;background:var(--blue);margin:12px auto 18px}
.how p{font-size:12px;line-height:1.7;color:var(--muted);margin-bottom:12px}

/* why */
.why{height:440px;background:var(--light);text-align:center;padding-top:40px}
.benefits{display:flex;justify-content:center;gap:36px;margin:30px 0 34px}
.benefit{width:140px}
.benefit .ic{width:78px;height:78px;border-radius:50%;margin:0 auto 14px;display:flex;align-items:center;justify-content:center}
.benefit span{font-size:12px;line-height:1.4;color:var(--ink);font-weight:600}

/* testimonial */
.testimonial{height:400px;background:linear-gradient(180deg,var(--navy-2),var(--navy));color:var(--white);text-align:center;padding:50px 170px 0}
.quote-ic{width:64px;height:64px;border-radius:50%;background:var(--blue);margin:0 auto 28px;display:flex;align-items:center;justify-content:center}
.testimonial p{font-size:13px;line-height:1.8;font-style:italic}
.testimonial .who{margin-top:18px;font-weight:700;font-size:13px;font-style:normal}
.testimonial .who small{display:block;font-weight:400;opacity:.8}

/* footer form */
.footer-form{height:160px;background:var(--blue);color:var(--white);text-align:center;padding-top:16px}
.footer-form h3{font-size:28px;font-weight:800;text-transform:uppercase}
.footer-form p{font-size:11px;margin-top:2px}
.row{display:flex;justify-content:center;gap:12px;margin-top:14px}
.row .field{width:210px;background:var(--white);margin:0}
.row .btn{padding:9px 18px;font-size:12px}
.copy{font-size:10px;margin-top:12px;opacity:.85}
</style>
</head>
<body>

<header class="hero">
  <div class="hero-photo" role="img" aria-label="City skyline at dusk behind a blue tint"></div>
  <div class="topbar">
    <div class="brand"><span class="mark"></span>BOP</div>
    <div class="contact">Call Now: <b>1-800-555-0142</b><br>Mon–Fri 9am–5pm PST</div>
  </div>
  <div class="hero-copy">
    <h1>Attract More <strong>Customer</strong></h1>
    <p>Who Spend More Money With Your Business Using Free Vacation &amp; Cruise Certificates And Other Incentives Without Breaking The Bank!</p>
  </div>
  <form class="lead-form">
    <div class="head"><h3>Enter Your Info!</h3><p>To be forwarded to our website to see<br>all the details and to receive your samples</p></div>
    <div class="body">
      <div class="field">Name</div>
      <div class="field">Email</div>
      <div class="field">Phone</div>
      <div class="btn">Download Free Samples<br>of Our Incentives</div>
    </div>
  </form>
</header>

<section class="imagine">
  <svg class="curve" width="1200" height="62" viewBox="0 0 1200 62" aria-hidden="true"><path d="M0 62 L0 40 Q600 -20 1200 20 L1200 62 Z" fill="#1b75c9"/></svg>
  <div class="imagine-copy">
    <h2>Imagine</h2>
    <p>Being able to hand out real travel and leisure gifts that cost you pennies yet make your customers feel valued and ready to buy again and again.</p>
    <p>Bright Oak Promotions Group has provided high-perceived-value promotional incentives to businesses of every size for years, helping them boost sales, reward loyalty and stand out from every other competitor in town.</p>
    <p>Our incentives are easy to use, fully printable and backed by friendly support so your team can start today.</p>
    <div class="btn">Download Free Samples<br>of Our Incentives</div>
  </div>
  <div class="samples" role="img" aria-label="Fanned stack of printed vacation and cruise certificate samples"></div>
  <div class="imagine-name">Bright Oak Promotions Group</div>
</section>

<section class="how">
  <h2 class="sec-title">How Can We Do It</h2>
  <div class="dot"></div>
  <p>We have partnered with resorts, cruise lines and hotels around the country to buy unused inventory in bulk. That lets us pass these amazing vacation packages to you at a tiny fraction of retail, so you can offer a gift that feels generous while keeping your marketing budget firmly under control.</p>
  <p>We also help you decide where each incentive fits best, from closing a sale to rewarding referrals and bringing past customers back through your door.</p>
  <div class="btn">Download Free Samples<br>of Our Incentives</div>
</section>

<section class="why">
  <h2 class="sec-title">Why Offer Incentives To Customers?</h2>
  <div class="benefits">
    <div class="benefit"><div class="ic" style="background:#1b75c9"><svg width="34" height="34" viewBox="0 0 34 34"><path d="M17 4 L29 18 H21 V30 H13 V18 H5 Z" fill="#fff"/></svg></div><span>Increase Response Over Any Existing Ads</span></div>
    <div class="benefit"><div class="ic" style="background:#27a9a1"><svg width="34" height="34" viewBox="0 0 34 34"><path d="M6 18 L14 26 L29 9" stroke="#fff" stroke-width="4" fill="none"/></svg></div><span>Hit Sales Closing Tool – Gift to Purchase</span></div>
    <div class="benefit"><div class="ic" style="background:#4caf50"><svg width="34" height="34" viewBox="0 0 34 34"><path d="M17 3 L21 13 L31 13 L23 20 L26 30 L17 24 L8 30 L11 20 L3 13 L13 13 Z" fill="#fff"/></svg></div><span>Build Brand Awareness and Trust</span></div>
    <div class="benefit"><div class="ic" style="background:#f39a1e"><svg width="34" height="34" viewBox="0 0 34 34"><rect x="5" y="18" width="6" height="12" fill="#fff"/><rect x="14" y="11" width="6" height="19" fill="#fff"/><rect x="23" y="4" width="6" height="26" fill="#fff"/></svg></div><span>Stand Out And Beat Your Competition</span></div>
    <div class="benefit"><div class="ic" style="background:#8e44ad"><svg width="34" height="34" viewBox="0 0 34 34"><circle cx="17" cy="12" r="6" fill="#fff"/><path d="M5 30 Q17 14 29 30 Z" fill="#fff"/></svg></div><span>Boost Repeat and Referral Business</span></div>
    <div class="benefit"><div class="ic" style="background:#e74c8c"><svg width="34" height="34" viewBox="0 0 34 34"><path d="M4 26 L12 16 L19 21 L30 7" stroke="#fff" stroke-width="4" fill="none"/></svg></div><span>Improve Retention Rates</span></div>
  </div>
  <div class="btn">Download Free Samples<br>of Our Incentives</div>
</section>

<section class="testimonial" role="img" aria-label="Testimonial over a dark blue city photo">
  <div class="quote-ic"><svg width="30" height="28" viewBox="0 0 30 28"><path d="M3 3 H27 V19 H12 L6 25 V19 H3 Z" fill="#fff"/></svg></div>
  <p>“I always believed incentives were just gimmicks until I tried these vacation certificates. Sales increased nearly a third in the first quarter, and customers keep coming back to tell me about their trips. The value we offer is real, the cost is tiny, and my team finally has an easy way to close the deal without slashing prices. I recommend this program to every business owner I know who wants real growth.”</p>
  <div class="who">Dana Kell<small>Kell Home Outfitters</small></div>
</section>

<section class="footer-form">
  <h3>Enter Your Info!</h3>
  <p>To be forwarded to our website for all the details and to receive your samples</p>
  <div class="row">
    <div class="field">Name</div>
    <div class="field">Email</div>
    <div class="field">Phone</div>
    <div class="btn">Download Free Samples</div>
  </div>
  <div class="copy">© Bright Oak Promotions Group. All rights reserved.</div>
</section>

</body>
</html>
```